Garden Maintenance business card

I need a business card design for my new business "Silver Birch Garden Co". I do garden maintenance including lawns, turf lawn, pruning, hedging, water systems, anything related to the garden really (dont think i need to include any of that except garden maintenance)

Reason: narrowed it down and just showing my business partners the designs, cheers

Industry/Entity Type

Business

Requirements
Must have
• Must Have:
- ABN: XX XXX XXX XXX
Mobile phone number 00 0000000
email address xxxx.xxxxxx@sbgco.net
Owner Name Xxxx xxxxxx
title: garden specialist possibly under name or something sounding professional
logo which has been submitted both with a background and one without, feel free to choose whichever one you like
business name

```html
<!DOCTYPE html>
<html lang="en">
<head>
<meta charset="utf-8">
<title>Silver Birch Garden Co – Business Card</title>
<link href="https://fonts.googleapis.com/css2?family=Questrial&display=swap" rel="stylesheet">
<style>
  :root {
    --card-white: #ffffff;
    --leaf-green: #6cc417;
    --band-green: #7fe000;
    --band-green-light: #97f21a;
    --ink: #1f1f1f;
    --text-on-band: #ffffff;
  }
  html, body {
    margin: 0;
    padding: 0;
    overflow: hidden;
    background: var(--card-white);
  }
  .card {
    position: relative;
    width: 1200px;
    height: 694px;
    background: var(--card-white);
    overflow: hidden;
    font-family: "Questrial", "Century Gothic", sans-serif;
  }
  .brand {
    position: absolute;
    left: 240px;
    top: 128px;
    display: flex;
    align-items: center;
    gap: 14px;
  }
  .brand-dot {
    width: 30px;
    height: 30px;
    border-radius: 50%;
    background: var(--leaf-green);
  }
  .brand-name {
    font-size: 36px;
    color: var(--leaf-green);
    line-height: 1;
  }
  .owner-name {
    position: absolute;
    left: 362px;
    top: 250px;
    margin: 0;
    font-size: 80px;
    font-weight: 400;
    line-height: 1;
    color: var(--leaf-green);
    white-space: nowrap;
  }
  .owner-title {
    position: absolute;
    left: 411px;
    top: 340px;
    margin: 0;
    font-size: 50px;
    line-height: 1;
    color: var(--ink);
    white-space: nowrap;
  }
  .contact-band {
    position: absolute;
    left: 0;
    top: 422px;
    width: 1200px;
    height: 272px;
    background: radial-gradient(ellipse at 40% 40%, var(--band-green-light), var(--band-green) 70%);
  }
  .contact-list {
    position: absolute;
    left: 0;
    top: 448px;
    width: 1200px;
    margin: 0;
    padding: 0;
    list-style: none;
    text-align: center;
    color: var(--text-on-band);
    font-size: 43px;
    line-height: 53px;
    white-space: nowrap;
  }
</style>
</head>
<body>
  <main class="card">
    <div class="brand">
      <span class="brand-dot"></span>
      <span class="brand-name">Silver Birch Garden Co</span>
    </div>

    <h1 class="owner-name">Owner Name</h1>
    <p class="owner-title">garden specialist</p>

    <div class="contact-band" role="img" aria-label="Bright green band with a soft wavy leaf-stripe pattern"></div>

    <ul class="contact-list">
      <li>- ABN: XX XXX XXX XXX</li>
      <li>Mobile phone number 00 0000000</li>
      <li>email address xxxx.xxxxxx@sbgco.net</li>
    </ul>
  </main>
</body>
</html>
```